Vodka label for New Brand called HOLT Vodka

We need a label measuring 3.5 inches wide & 5 inches tall for this vodka bottle. The brand is "HOLT Vodka". This should be the largest font on the label. "Handcrafted in the USA" should be on bottle in small font near the bottom. The tagline "Here's Our Liquid Toast" also needs to be included anywhere that makes sense in a smaller font than the brand name. Also in smaller font at the bottom/corners- "80 proof, 750 ml, 40% alc/vol" I value the human mind over AI, but am providing a couple designs that were AI generated to give you a better idea where to start and what we are looking for. Thank you!
Updates

Target Market(s)

21-45 year olds.

Industry/Entity Type

Alcohol

Colors
0054AA
0677BA
7BADD7
CADEEF
E8F1F8
EB3D1F
EC4F4E
F09395
F8D3D4
FCEDEE

Requirements
Should not have
• You can not use the US flag but can use elements of it.

```html
<!DOCTYPE html>
<html lang="en">
<head>
<meta charset="utf-8">
<title>HOLT Vodka — Bottle Label</title>
<link rel="stylesheet" href="https://fonts.googleapis.com/css2?family=Exo+2:wght@800&family=Saira+Condensed:wght@800&family=Montserrat:wght@400;700&display=swap">
<style>
  :root {
    --navy: #011e4b;
    --navy-light: #2a4470;
    --star-tone: #6a7894;
    --red: #ff0000;
    --white: #ffffff;
    --stripe-h: 92px;
  }
  * { box-sizing: border-box; margin: 0; padding: 0; }
  html, body { width: 900px; height: 1200px; overflow: hidden; background: var(--white); }

  .label {
    position: relative;
    width: 900px;
    height: 1200px;
    overflow: hidden;
    background: var(--white);
  }

  /* Upper navy field */
  .canton {
    position: absolute;
    left: 0; top: 0;
    width: 900px; height: 466px;
    background: var(--navy);
  }
  .canton__stars {
    position: absolute;
    left: 6px; top: 16px;
    width: 888px; height: 420px;
    background: linear-gradient(180deg, var(--navy-light) 0%, #1d3663 50%, var(--navy-light) 100%);
    opacity: 0.75;
  }

  .brand {
    position: absolute;
    left: 0; right: 0;
    text-align: center;
    color: var(--white);
  }
  .brand__name {
    top: 86px;
    font-family: "Exo 2", sans-serif;
    font-weight: 800;
    font-size: 238px;
    line-height: 1;
    letter-spacing: 2px;
  }
  .brand__type {
    top: 318px;
    font-family: "Exo 2", sans-serif;
    font-weight: 800;
    font-size: 82px;
    line-height: 1;
    letter-spacing: 42px;
    padding-left: 42px;
  }

  /* Stripes */
  .stripe {
    position: absolute;
    left: 0;
    width: 900px;
    height: var(--stripe-h);
    background: var(--red);
  }
  .stripe--1 { top: 558px; }
  .stripe--2 { top: 742px; }
  .stripe--3 { top: 925px; }
  .stripe--4 { top: 1108px; }

  /* Tagline panel */
  .tagline {
    position: absolute;
    left: 190px; top: 528px;
    width: 520px; height: 152px;
    background: var(--white);
    border: 7px solid var(--red);
    display: flex;
    align-items: center;
    justify-content: center;
    text-align: center;
    font-family: "Saira Condensed", sans-serif;
    font-weight: 800;
    font-size: 54px;
    line-height: 0.98;
    color: var(--navy);
    text-transform: uppercase;
  }

  /* Bottom info */
  .origin {
    position: absolute;
    left: 253px; top: 1092px;
    width: 395px; height: 116px;
    background: var(--white);
    border: 5px solid var(--navy);
    text-align: center;
    padding-top: 12px;
    font-family: "Montserrat", sans-serif;
  }
  .origin__made {
    color: var(--red);
    font-weight: 700;
    font-size: 27px;
    line-height: 1;
    word-spacing: 4px;
  }
  .origin__abv {
    margin-top: 4px;
    color: var(--navy);
    font-weight: 400;
    font-size: 25px;
    letter-spacing: 4px;
    line-height: 1.1;
  }

  .spec {
    position: absolute;
    top: 1138px;
    font-family: "Montserrat", sans-serif;
    font-weight: 400;
    font-size: 27px;
    line-height: 1;
    color: var(--navy);
  }
  .spec--proof { left: 12px; }
  .spec--volume { right: 28px; }
</style>
</head>
<body>
  <main class="label">
    <section class="canton">
      <div class="canton__stars" role="img" aria-label="Grid of soft blue-grey stars on navy"></div>
    </section>

    <h1 class="brand brand__name">HOLT</h1>
    <p class="brand brand__type">VODKA</p>

    <div class="stripe stripe--1"></div>
    <div class="stripe stripe--2"></div>
    <div class="stripe stripe--3"></div>
    <div class="stripe stripe--4"></div>

    <p class="tagline">Here's Our Liquid<br>Toast</p>

    <div class="origin">
      <p class="origin__made">HANDCRAFTED<br>IN THE USA</p>
      <p class="origin__abv">40% ALC/VOL</p>
    </div>

    <p class="spec spec--proof">80 PROOF</p>
    <p class="spec spec--volume">750ml</p>
  </main>
</body>
</html>
```